Colourful Bold Design for Pet Insurance Website

PLEASE NOTE THAT THIS PROJECT HAS BEEN EXTENDED. Please read the PROJECT EXTENSION DOCUMENT BEFORE STARTING WORK ON ANY DESIGNS.

We are looking for a colourful bold new template design for our JOOMLA HOMEPAGE and a matching design for our new WORDPRESS BLOG.

The website will help pet owners work out which insurance policy best meets their needs. The aim of the website is to explain policy differences in a plain clear manner.

The website will need to have a professional colourful image. It needs to be BOLD, CLEAN AND SHARP rather than soft, pastel and cuddly.

COLOUR SCHEME
The website needs to have a bold colourful design on a white background.
On the inner pages we will have five different types of policies which will be colour coded. We would ideally therefore like to incorporate five distinct colours in the design. See attached document for example of colour schemes we like.

LOGO
We want to keep the existing logo. Please find the file attached. You may though change the logo colours.

CONTENT
One of the reasons for the new design is that we want to change the style of the homepage and include new content. Our current homepage can be found at www.furrow-cover-polls.co.uk.

Content Required
Slideshow
Article Intro.. About Pet Insurance
Policy Lookup Box (see existing site… you can change the design of this)
Six link options (see links on left of current page)
Latest Reviews (List of 6)
Ad (Same dimensions as currently on homepage)

News and Comment Section - To include Three or Four Articles, Title, Intro to article (probably 3 or 4 lines .. about 400px wide), Read more link
Social Media Section
Chatterbook Plugin with Feed
Latest Tweets Plugin
Pet Charities Latest Tweets
Footer
Larger footer with lots of links grouped in sections

It does not need to include the clipart pic of the pets which is on the current homepage.

Examples of Websites and Templates We Like
http://www.pawlane.com/ (like colours… fonts…layout)
http://sitetheme.brightkiln.com/?template=upbeat&path=/... (like the clarity, "white" space etc)
http://www.layoutforge.com/demo/51872.html (like white space, clear easy to read fonts… don’t like colour scheme, size of top picture)
http://www.layoutforge.com/website-templates/63915.html (like colour scheme, use of white space)

FEEDBACK
I will provide lots of feedback on all designs submitted so that together we can get the best result.

For clarification this is a DESIGN ONLY project. Our website developer will view the designs before we make our final choice as he wants to ensure he can develop "sharp, practical and most importantly light weight web interface" from the design.

Just updated this brief to clarify design issues, content issues and to give some more examples of site designs I like. 

Please note that although we wish to keep the logo you can change the colours to suit your design. 

Please note that we have now added details of pictures we would be happy to use on the website.  We would prefer it if you used one of these.   Otherwise please ensure your picture includes a nice dog and nice cat and no people!

I have been delighted with the quality of the designs submitted for this project.  So much so that I am going to extend the project to include some additional inner pages.   The amended brief will be posted on here on Friday 10 May.   The deadline will be extended and the budget will also be increased. 

Reason: Additional inner pages now required. Budget will be increased. Revised brief to be posted on here Friday 10 May.

Target Market(s)

Pet owners in the UK who are confused about pet insurance. It therefore needs to be a bold design which is plain, clean and easy to read. It should use bold colours rather than pastels and should not use "cuddly" images.

Industry/Entity Type

Insurance

Requirements
Must have
• Bold clear and distinct colours (preferably 5)
Content as per uploaded file (not just content from existing site)
Easy to read fonts
Should not have
• Pastel colours
Cuddly images

```html
<!DOCTYPE html>
<html lang="en">
<head>
<meta charset="utf-8">
<title>Furrow Cover Polls UK</title>
<link href="https://fonts.googleapis.com/css2?family=Arvo:wght@400;700&family=Open+Sans:wght@400;600;700&display=swap" rel="stylesheet">
<style>
:root{
  --sky:#1b93c3;
  --navy:#0d5f86;
  --navy-deep:#0a4f71;
  --pink:#d4157f;
  --orange:#f47b20;
  --link-blue:#1478b8;
  --green:#3e9a1f;
  --ink:#4a4a4a;
  --panel:#f2f2f2;
  --page:#ececec;
  --footer:#222324;
  --footer-text:#bdbdbd;
  --white:#fff;
}
*{box-sizing:border-box;margin:0;padding:0}
html,body{width:924px;height:1200px;overflow:hidden}
body{position:relative;background:var(--page);font-family:"Open Sans",Arial,sans-serif;color:var(--ink);font-size:9.5px;line-height:1.45}
a{text-decoration:none}
.top-band{position:absolute;left:0;top:0;width:924px;height:170px;background:var(--sky)}
.header{position:absolute;left:100px;top:0;width:724px;height:170px}
.header-strip{position:absolute;left:0;top:0;width:724px;height:84px;background:#1a8cbb}
.lookup-band{position:absolute;left:0;top:84px;width:724px;height:92px;background:linear-gradient(#0e6790,var(--navy-deep))}
.flap{position:absolute;top:170px;width:0;height:0;border-top:24px solid var(--navy-deep)}
.flap.left{left:100px;border-left:13px solid transparent}
.flap.right{left:811px;border-right:13px solid transparent}
.brand{position:absolute;left:13px;top:18px;display:flex;align-items:center;gap:8px}
.brand-dot{width:30px;height:30px;border-radius:50%;background:var(--orange)}
.brand-name{color:var(--white);font-weight:700;font-size:17px;line-height:1.05;width:130px}
.site-search{position:absolute;left:496px;top:19px;display:flex;align-items:center;gap:7px;color:var(--white);font-size:13px}
.site-search .field{width:166px;height:19px;background:var(--white);border:1px solid #c9d7de;border-radius:2px;position:relative}
.field svg{position:absolute;left:5px;top:5px}
.main-nav{position:absolute;left:206px;top:57px;display:flex;gap:26px}
.main-nav a{color:var(--white);font-weight:700;font-size:10.5px;letter-spacing:.1px}
.lookup-title{position:absolute;left:15px;top:99px;font-family:Arvo,Georgia,serif;color:var(--white);font-size:17px}
.lookup-form{position:absolute;left:15px;top:127px;display:flex;gap:8px}
.select{height:20px;background:#f4f4f4;border:1px solid #bbb;border-radius:2px;position:relative;font-size:9px;color:#888;padding:3px 0 0 20px}
.select.policy-a{width:116px}.select.policy-b{width:116px}
.select .caret{position:absolute;right:3px;top:3px;width:12px;height:12px;border:1px solid #888;background:#eee}
.select .caret:after{content:"";position:absolute;left:2px;top:4px;border:3px solid transparent;border-top:4px solid #333}
.search-btn{margin-left:6px;width:79px;height:21px;background:var(--orange);color:var(--white);font-weight:700;font-size:10px;text-align:center;line-height:21px;border-radius:2px}
.content{position:absolute;left:113px;top:176px;width:698px;height:880px;background:var(--white);box-shadow:0 0 3px rgba(0,0,0,.15)}
.content-topline{position:absolute;left:113px;top:176px;width:698px;height:6px;background:#dcdcdc}
.hero{position:absolute;left:128px;top:190px;width:667px;height:181px;background:linear-gradient(90deg,#eeeae6 0%,#e9e2db 55%,#d8b89a 80%,#b9956f 100%)}
.hero-pic{position:absolute;right:0;top:0;width:340px;height:181px;background:linear-gradient(90deg,rgba(240,220,195,0) 0%,#e6c3a0 35%,#4a3b36 60%,#c79c63 100%)}
.hero-copy{position:absolute;left:23px;top:24px;font-family:Arvo,Georgia,serif;font-size:18.5px;line-height:24.5px;color:#454545}
.hero-copy em{font-style:normal;color:var(--orange)}
.dots{position:absolute;left:23px;top:150px;display:flex;gap:6px}
.dots i{width:8px;height:8px;border-radius:50%;background:#555}
.dots i:first-child{background:var(--orange)}
.card{position:absolute;width:217px;height:81px;background:var(--panel);padding:5px 8px}
.card h3{font-family:Arvo,Georgia,serif;font-weight:400;color:var(--pink);font-size:14.5px;line-height:18px;margin-bottom:3px}
.card p{font-size:9px;line-height:12.5px}
.more{display:block;color:var(--orange);font-weight:700;font-size:9px;margin-top:2px}
.divider{position:absolute;left:595px;top:391px;width:1px;height:640px;background:#e2e2e2}
.welcome{position:absolute;left:127px;top:663px;width:455px}
.welcome .small{font-family:Arvo,Georgia,serif;font-size:14px;color:#333;line-height:16px}
.welcome h1,.welcome h2{font-family:Arvo,Georgia,serif;color:var(--navy);font-size:16px;line-height:19px;margin-bottom:8px}
.welcome h2{font-size:14.5px;margin:14px 0 6px}
.welcome p{font-size:9px;line-height:12.5px;margin-bottom:10px}
.welcome a{color:var(--green)}
.ad{position:absolute;left:615px;top:391px;width:180px;height:179px;background:#efefef;display:flex;align-items:center;justify-content:center;text-align:center;font-family:Arvo,Georgia,serif;font-size:16px;color:#9a9a9a;line-height:18px}
.news{position:absolute;left:615px;top:585px;width:182px}
.news h2{font-family:Arvo,Georgia,serif;font-weight:400;color:var(--pink);font-size:14.5px;margin-bottom:4px}
.news h4{color:var(--link-blue);font-size:9.5px;font-weight:600;line-height:12px}
.news p{font-size:9px;line-height:12.5px}
.news .more{margin:3px 0 8px}
.social-box{position:absolute;left:615px;top:747px;width:171px;height:150px;border:1px solid #c8c8c8;background:var(--white)}
.social-box h5{background:#f0f0f0;border-bottom:1px solid #ddd;font-size:9.5px;color:#333;padding:5px 8px;font-weight:700}
.fans{display:grid;grid-template-columns:repeat(4,36px);gap:5px 4px;padding:5px 8px 0}
.fan{font-size:7px;color:#888;text-align:center}
.fan span{display:block;width:36px;height:36px;margin-bottom:1px}
.plugin-note{font-size:7px;color:#555;padding:3px 8px;display:flex;align-items:center;gap:3px}
.plugin-note i{width:8px;height:8px;background:#3b5a98}
.tweets-head{position:absolute;left:615px;top:912px;display:flex;align-items:center;gap:8px;color:var(--link-blue);font-size:9.5px;font-weight:600}
.tweets-head i{width:17px;height:17px;background:#29a8e0;border-radius:3px}
.tweets{position:absolute;left:615px;top:942px;width:180px;height:89px;border:1px solid #8ccbe6;background:#eef7fb;padding:6px 8px}
.tweet{display:flex;gap:6px;padding-bottom:5px;margin-bottom:5px;border-bottom:1px dotted #aac}
.tweet:last-of-type{border:0}
.tweet i{width:18px;height:18px;border-radius:50%;background:var(--navy);flex:none;margin-top:3px}
.tweet p{font-size:7.5px;line-height:10px;color:#444}
.tweet b{color:#29a0d8;font-weight:600}
.tweet u{color:#29a0d8}
.follow{position:absolute;right:6px;bottom:4px;font-size:7.5px;color:#29a0d8}
.footer-rule{position:absolute;left:0;top:1035px;width:924px;height:5px;background:var(--link-blue)}
.footer{position:absolute;left:0;top:1040px;width:924px;height:160px;background:var(--footer)}
.frame-corner{position:absolute;top:1018px;width:43px;height:42px;border:5px solid var(--link-blue)}
.frame-corner.left{left:105px;border-right:0;border-top:0}
.frame-corner.right{left:776px;border-left:0;border-top:0}
.frame-fill{position:absolute;left:110px;top:1018px;width:704px;height:37px;background:var(--white)}
.foot-col{position:absolute;top:1080px;color:var(--footer-text);font-size:9px;line-height:13px}
.foot-col h6{font-family:Arvo,Georgia,serif;font-weight:400;color:var(--orange);font-size:12.5px;margin-bottom:10px}
.foot-col a{display:block;color:var(--footer-text)}
.follow-us{position:absolute;left:705px;top:1089px;color:var(--footer-text);font-size:10px;display:flex;align-items:center;gap:3px}
.follow-us i{width:11px;height:11px;border-radius:2px;margin-left:1px}
.foot-mark{position:absolute;left:752px;top:1125px;width:58px;height:58px;border-radius:50%;background:#3a3b3d}
</style>
</head>
<body>
<div class="top-band"></div>
<header class="header">
  <div class="header-strip"></div>
  <div class="lookup-band"></div>
  <div class="brand"><span class="brand-dot"></span><span class="brand-name">Furrow Cover Polls UK</span></div>
  <div class="site-search">Search
    <div class="field"><svg width="9" height="9" viewBox="0 0 9 9"><circle cx="3.6" cy="3.6" r="2.8" fill="none" stroke="#999" stroke-width="1.2"/><path d="M5.7 5.7L8.4 8.4" stroke="#999" stroke-width="1.3"/></svg></div>
  </div>
  <nav class="main-nav"><a>HOME</a><a>POLICIES</a><a>SURVEY REPORTS</a><a>FACT SHEET</a><a>GLOSSARY</a><a>NEWS</a><a>CONTACT US</a></nav>
  <div class="lookup-title">Check out a policy</div>
  <div class="lookup-form">
    <div class="select policy-a"><svg style="position:absolute;left:6px;top:5px" width="9" height="9" viewBox="0 0 9 9"><circle cx="3.6" cy="3.6" r="2.8" fill="none" stroke="#999" stroke-width="1.2"/><path d="M5.7 5.7L8.4 8.4" stroke="#999" stroke-width="1.3"/></svg>Brightpaw Cover<span class="caret"></span></div>
    <div class="select policy-b"><svg style="position:absolute;left:6px;top:5px" width="9" height="9" viewBox="0 0 9 9"><circle cx="3.6" cy="3.6" r="2.8" fill="none" stroke="#999" stroke-width="1.2"/><path d="M5.7 5.7L8.4 8.4" stroke="#999" stroke-width="1.3"/></svg>Select a Policy<span class="caret"></span></div>
    <div class="search-btn">SEARCH</div>
  </div>
</header>
<div class="flap left"></div><div class="flap right"></div>

<div class="frame-corner left"></div><div class="frame-corner right"></div>
<div class="footer-rule"></div>
<main class="content"></main>
<div class="content-topline"></div>

<section class="hero">
  <div class="hero-pic" role="img" aria-label="Photo of a fluffy apricot poodle beside two black puppies in a wicker basket"></div>
  <p class="hero-copy">An independent website…<br>dedicated to helping you …<br>find the <em>best insurance policy…</em><br>for your pet &nbsp;»</p>
  <div class="dots"><i></i><i></i><i></i><i></i><i></i><i></i></div>
</section>

<article class="card" style="left:128px;top:391px"><h3>Policy Files</h3><p>Full policy details including type of vet fees cover and limits, ratings, age limits, excess details, benefits and terms analysis.</p><a class="more">READ MORE</a></article>
<article class="card" style="left:361px;top:391px"><h3>Policy Search</h3><p>Exclusive to FCP friends. Search our database of more than 200 policies</p><a class="more">READ MORE</a></article>
<article class="card" style="left:128px;top:480px"><h3>Fact Sheets</h3><p>Learn about pet insurance. A little knowledge is essential to choosing the right policy.</p><a class="more" style="margin-top:14px">READ MORE</a></article>
<article class="card" style="left:361px;top:480px"><h3>Policy Listings by Type</h3><p>Full lists of continuous policies (aka "life time policies), 12- month policies and accident policies.</p><a class="more">READ MORE</a></article>
<article class="card" style="left:128px;top:571px"><h3>Claims Survey</h3><p>Made a claim in the last 12 months? Please help us to help others by completing this 2-minute survey.</p><a class="more">READ MORE</a></article>
<article class="card" style="left:361px;top:571px"><h3>2013 Price Survey Report</h3><p>Due April 2013.</p><a class="more">READ MORE</a></article>

<div class="divider"></div>

<section class="welcome">
  <div class="small">Welcome to</div>
  <h1>Furrow Cover Polls UK</h1>
  <p>This is an <a>independent</a> website dedicated to <a>helping you</a> to find the best pet insurance policy for your pet</p>
  <p>Here you will find <a>unbiased detailed information</a> about almost all of the <a>205 pet insurance policies</a> currently available in the UK (we hope the other 3 will follow shortly!)</p>
  <p>We do NOT sell any <a>pet insurance policies</a> nor do we receive commission from any insurance companies.</p>
  <h2>Getting started and finally</h2>
  <p>If you are new to pet insurance or find the different types of policy confusing then start by reading <a>Pet Insurance - An Introduction</a>.</p>
  <p>If you want more details on &nbsp;<a>a particular policy</a> then use the "Check out a policy" search box which is in the s sidebar. &nbsp;Be sure to look at all three pages (summary, benefits and terms).</p>
  <p>If you want to <a>identify suitable policies</a> then use the detailed search facility to produce a shortlist of policies which meet your criteria.</p>
  <p>All the information on this website is provided free of charge. &nbsp;We hope you will find it useful when looking for the best pet insurance policy for your pet.</p>
  <p>If you would like to help us all get the best insurance then please complete the <a>claims experience survey</a>. &nbsp;Your input will help us to provide <a>claims satisfaction ratings</a> and survey reports which in turn we hope will help pet owners when choosing policies for their pets.</p>
  <p><a>Working together we can get the best insurance cover for our pets!</a></p>
</section>

<aside class="ad">Advertising<br>Space</aside>

<section class="news">
  <h2>Latest News &amp; Comment</h2>
  <h4>About Furrow Cover Polls UK</h4>
  <p>Our mission is quite simple - to help you make the right choice about pet insurance for your pet.</p>
  <a class="more">READ MORE</a>
  <h4>An idea is born!</h4>
  <p>Certainly no time to read the small print before you buy a policy!</p>
  <a class="more">READ MORE</a>
</section>

<section class="social-box">
  <h5>Find us on Chatterbook</h5>
  <div class="fans">
    <div class="fan"><span role="img" aria-label="Member photo" style="background:#6f7d62"></span>Claudia</div>
    <div class="fan"><span role="img" aria-label="Member photo" style="background:#8a5a3c"></span>Andréa</div>
    <div class="fan"><span role="img" aria-label="Member photo" style="background:#8e8e8e"></span>Daniel</div>
    <div class="fan"><span role="img" aria-label="Member photo" style="background:#4a3d38"></span>Lorena</div>
    <div class="fan"><span role="img" aria-label="Member photo" style="background:#d88a3e"></span>JoAnn</div>
    <div class="fan"><span role="img" aria-label="Member photo" style="background:#9aa08a"></span>Jennifer</div>
    <div class="fan"><span role="img" aria-label="Member photo" style="background:#b58a86"></span>Tony</div>
    <div class="fan"><span role="img" aria-label="Member photo" style="background:#c9a48a"></span>Pat</div>
  </div>
  <div class="plugin-note"><i></i>Chatterbook social plugin</div>
</section>

<div class="tweets-head"><i></i>LATEST TWEETS</div>
<section class="tweets">
  <div class="tweet"><i></i><p><b>Sed sed risus</b><br>At justo convallis consectetur<br><u>tempor ornare sapien</u> ....</p></div>
  <div class="tweet"><i></i><p><b>Sed sed risus</b><br>At justo convallis consectetur<br><u>tempor ornare sapien</u> ....</p></div>
  <span class="follow">Follow</span>
</section>

<footer class="footer"></footer>
<div class="frame-fill" style="top:1035px;height:5px;background:var(--white)"></div>
<div class="foot-col" style="left:114px"><h6>Contacts</h6>Furrow Cover Polls UK<br>Open Monday - Friday 8am - 6pm<br><br>2468 Street Name, Suite C<br>City, United Sates</div>
<div class="foot-col" style="left:288px"><h6>Company Info</h6><a>Support and FAQ</a><a>Contact Us</a><a>Refund Policy</a><a>Privacy Policy</a></div>
<div class="foot-col" style="left:443px"><h6>Need Help?</h6><a>About Us</a><a>Legal</a><a>Sitemap</a></div>
<div class="follow-us">Follow us on : <i style="background:#3b5a98"></i><i style="background:#29a8e0"></i><i style="background:#f08a24"></i></div>
<div class="foot-mark"></div>
</body>
</html>
```